Harmony Four Showcase
Date: Sunday Oct 2, 2022
When: 2-4 p.m.
Location: Brindle9 Alehouse
413 Marigold Wy #200, Sacramento, CA 95821
Tickets: www.Ticketwisp.example
General seating: $15 for adults and $10 for students

```html
<!DOCTYPE html>
<html lang="en">
<head>
<meta charset="utf-8">
<title>Harmony Four Showcase</title>
<link rel="stylesheet" href="https://fonts.googleapis.com/css2?family=Yellowtail&family=Oswald:wght@500&family=Lora:ital,wght@0,400;1,400;1,500&family=Open+Sans:wght@400;700&display=swap">
<style>
  :root {
    --page-bg: #505050;
    --red-hot: #f0361b;
    --crimson: #b80a3a;
    --wine: #5c0038;
    --plum: #8a3d8f;
    --gold: #f9a314;
    --white: #ffffff;
    --rule: rgba(255,255,255,0.9);
  }
  * { margin: 0; padding: 0; box-sizing: border-box; }
  html, body { width: 1200px; height: 800px; overflow: hidden; }
  body { background: var(--page-bg); position: relative; }

  .banner {
    position: absolute; left: 20px; top: 110px;
    width: 1160px; height: 580px; overflow: hidden;
    background:
      radial-gradient(ellipse 60% 30% at 10% 100%, rgba(160,80,170,0.55), transparent 70%),
      radial-gradient(ellipse 40% 25% at 45% 95%, rgba(150,70,160,0.35), transparent 70%),
      linear-gradient(160deg, var(--red-hot) 0%, var(--crimson) 22%, #7a0040 48%, var(--wine) 75%, #4e003c 100%);
    color: var(--white);
  }

  .info { position: absolute; left: 0; top: 0; width: 585px; height: 100%; text-align: center; }

  .title-script {
    position: absolute; left: 0; right: 0; top: 62px;
    font-family: "Yellowtail", cursive; font-size: 64px; line-height: 1;
    color: var(--white);
  }
  .title-main {
    position: absolute; left: 0; right: 0; top: 140px;
    font-family: "Oswald", sans-serif; font-weight: 500; font-size: 82px; line-height: 1;
    color: var(--gold); letter-spacing: 1px;
  }

  .when {
    position: absolute; left: 165px; top: 248px; display: flex; align-items: center;
  }
  .when-year {
    font-family: "Lora", serif; font-size: 54px; line-height: 1; color: var(--gold);
    padding-right: 10px; border-right: 2px solid var(--white);
  }
  .when-detail { padding-left: 10px; text-align: left; font-family: "Lora", serif; font-style: italic; }
  .when-day { font-size: 21px; color: var(--gold); line-height: 1.2; }
  .when-time { font-size: 26px; color: var(--white); font-weight: 500; line-height: 1.2; }

  .venue {
    position: absolute; left: 0; right: 0; top: 318px;
    font-family: "Open Sans", sans-serif; font-size: 19px; line-height: 24px;
  }

  .pricing {
    position: absolute; left: 63px; top: 382px; width: 461px; height: 46px;
    border-top: 1.5px solid var(--rule); border-bottom: 1.5px solid var(--rule);
    display: flex; align-items: center;
    font-family: "Open Sans", sans-serif; font-weight: 700;
  }
  .pricing-type {
    width: 122px; height: 100%; border-right: 1.5px solid var(--rule);
    color: var(--gold); font-size: 18px; line-height: 19px;
    display: flex; align-items: center; justify-content: center; text-align: left;
  }
  .pricing-tier { display: flex; align-items: baseline; margin-left: 12px; }
  .pricing-tier + .pricing-tier { margin-left: 22px; }
  .tier-label { font-size: 17px; color: var(--white); margin-right: 9px; letter-spacing: 0.5px; }
  .tier-price { font-size: 28px; color: var(--gold); }

  .booking {
    position: absolute; left: 0; right: 0; top: 446px;
    font-family: "Open Sans", sans-serif; font-weight: 700; font-size: 30px; letter-spacing: 1px;
  }
  .booking-url {
    position: absolute; left: 0; right: 0; top: 490px;
    font-family: "Open Sans", sans-serif; font-size: 24px; letter-spacing: 7px;
  }
  .booking-url .brand { color: var(--gold); }

  .stage-art {
    position: absolute; left: 542px; top: 60px; width: 618px; height: 520px;
    background:
      radial-gradient(ellipse 45% 55% at 58% 55%, rgba(245,130,40,0.55), transparent 70%),
      radial-gradient(ellipse 60% 14% at 55% 92%, rgba(210,40,50,0.7), transparent 75%),
      linear-gradient(180deg, rgba(230,90,60,0.18), rgba(120,20,70,0.1));
  }
</style>
</head>
<body>
  <main class="banner">
    <section class="info">
      <h1>
        <span class="title-script">Harmony Four</span>
        <span class="title-main">SHOWCASE</span>
      </h1>

      <div class="when">
        <div class="when-year">2022</div>
        <div class="when-detail">
          <div class="when-day">Sunday Oct 2</div>
          <div class="when-time">At 2-4 p.m.</div>
        </div>
      </div>

      <address class="venue" style="font-style:normal">
        Brindle9 Alehouse<br>
        413 Marigold Wy #200, Sacramento, CA 95821
      </address>

      <div class="pricing">
        <div class="pricing-type">GENERAL<br>SEATING</div>
        <div class="pricing-tier"><span class="tier-label">ADULTS</span><span class="tier-price">$15</span></div>
        <div class="pricing-tier"><span class="tier-label">STUDENTS</span><span class="tier-price">$10</span></div>
      </div>

      <div class="booking">BOOKING ON</div>
      <div class="booking-url">www.<span class="brand">Ticketwisp</span>.example</div>
    </section>

    <div class="stage-art" role="img" aria-label="Illustration of a vintage microphone, double bass, saxophone and trumpet on a lit stage under spotlights"></div>
  </main>
</body>
</html>
```